Flyer-Design für Kultursalon
Wir haben einen sehr edel wirkenden Programmflyer erhalten. Halberg hat all unsere Änderungwünsche zügig umgesetzt. Wir sind sehr zufrieden!
Zielgruppe
Wir, das Villa Morena, sind ein neuer Kultursalon in Bad Solmingen. Wir haben eine Kleinkunstbühne geschaffen, die wir Ende Oktober eröffnen wollen. Zukünftig sollen hier Konzerte, Lesungen, Kabarett, Comedy, Impro-Theater, Tango-Salons und Weinveranstaltungen stattfinden. Ansprechen wollen wir ein möglichst breites Publikum: Kulturinteresserte Menschen zwischen ca. 30-90 Jahren, das Gros des Publkums wird vermutlich zwischen 40 und 75 Jahren sein. Hinzu kommen touristische Gäste aus der Kur- und Wellnessstadt Bad Solmingen.
Aufgabenstellung
Wir brauchen einen schicken Programmflyer, den wir ca. alle drei Monate wechseln können. Zum Start soll das Programm für vier Monate - Oktober (nur Eröffnungswochenende), November, Dezember und Januar draufkommen, weil wir zu Beginn noch nicht so viele Veranstaltungen geplant haben. Mittelfristig ist anvisiert, bis zu acht Veranstaltungen pro Monat anzubieten. Abgebildet werden soll jeweils ein Foto des oder der Künstler, sowie ein kurzer Text zum Programm. Dazu natürlich Informationen wie Villa Morena (Ort und Adresse), Tickets über Karten Direkt sowie weitere Infos auf unserer Website www.villa-morena-kulturhaus.de
Die Farben Rot, Grau und Schwarz kehren sowohl auf unserer Website als auch im Kultursalon selbst immer wieder und sollten auch im Flyer eine Rolle spielen.

```html
<!DOCTYPE html>
<html lang="de">
<head>
<meta charset="utf-8">
<title>Villa Morena – Programm</title>
<link href="https://fonts.googleapis.com/css2?family=Roboto+Condensed:ital,wght@0,300;0,400;1,800&display=swap" rel="stylesheet">
<style>
:root{
  --slate:#4a4d4f;
  --slate-dark:#3b3c3e;
  --white:#ffffff;
  --red:#d7141a;
  --frame:rgba(255,255,255,.85);
}
*{margin:0;padding:0;box-sizing:border-box}
html,body{width:1200px;height:2833px;overflow:hidden;background:var(--slate)}
body{font-family:"Roboto Condensed",sans-serif;color:var(--white);position:relative}
.cell{position:absolute;width:400px;height:564px;overflow:hidden}
.c1{left:0}.c2{left:400px}.c3{left:800px}
.r1{top:0}.r2{top:564px}.r3{top:1128px;height:569px}.r4{top:1697px;height:553px}
.text-cell{background:var(--slate);padding:0 50px 0 52px}
.frame{position:absolute;border:1.5px solid var(--frame);pointer-events:none;width:328px}
.date{font-weight:300;font-size:23px;margin-top:28px}
.title{font-weight:800;font-style:italic;font-size:25px;line-height:1.12;margin-top:24px}
.desc{font-weight:300;font-size:20px;line-height:24px;margin-top:24px;text-align:justify;hyphens:auto;-webkit-hyphens:auto}
.desc.left{text-align:left}
.quote-cell{background:var(--slate-dark);display:flex;flex-direction:column;justify-content:center;align-items:flex-end;text-align:right;padding-right:54px}
.quote{font-weight:800;font-style:italic;font-size:25px;line-height:1.15}
.quote-author{font-weight:800;font-style:italic;font-size:25px;margin-top:32px}
.footer{position:absolute;top:2250px;left:0;width:1200px;height:583px;background:var(--slate)}
.footer-photo{position:absolute;left:0;top:0;width:760px;height:583px}
.venue{position:absolute;right:36px;top:22px;text-align:right}
.venue-name{font-weight:300;font-size:100px;line-height:.98}
.venue-tag{font-weight:300;font-size:23px;margin-top:12px;opacity:.9}
.info{position:absolute;right:48px;text-align:right;font-weight:300;font-size:20px;line-height:24px}
.sponsor-label{position:absolute;left:570px;top:2648px;width:222px;text-align:right;font-weight:300;font-size:20px;line-height:24px}
.sponsor{position:absolute;left:553px;top:2703px;width:249px;height:100px;display:flex;align-items:center;gap:14px;padding-left:22px}
.sponsor-mark{width:22px;height:22px;background:var(--red)}
.sponsor-name{font-weight:400;font-size:25px;line-height:1.1}
</style>
</head>
<body>

<svg class="cell c1 r1" role="img" aria-label="Porträtfoto der Autorin mit Hut vor warmem Hintergrund"><defs><linearGradient id="g1" x1="0" y1="0" x2="1" y2="1"><stop offset="0" stop-color="#e6b66a"/><stop offset=".6" stop-color="#6b4a34"/><stop offset="1" stop-color="#2a2624"/></linearGradient></defs><rect width="400" height="564" fill="url(#g1)"/></svg>
<section class="cell c2 r1 text-cell">
  <p class="date">14. 1. 2022, 19.30 Uhr:</p>
  <h2 class="title">Marlene Vogt, „Mord &amp; Merlot – Giftiger Rotwein trifft Todes-Trüffel“</h2>
  <p class="desc">Was gibt es Genussvolleres als die Kombination von Wein und Schokolade – eine Mischung, die die Sinne anregt und die (Mord-)Fantasie beflügelt? Dass heiße Schokolade eine tödliche Waffe sein kann, dass Orangenlikörpralinen verknöcherte Jungfrauen zum Erblühen bringen und dass die Leidenschaft für guten Wein wahre Affekthandlungen auslösen kann, all das weiß Marlene Vogt in diesem süß-herben Programm zu berichten. (Lesung mit Weinverkostung)</p>
</section>
<svg class="cell c3 r1" role="img" aria-label="Porträtfotos der Musikerin und des Musikers nebeneinander"><defs><linearGradient id="g2" x1="0" y1="0" x2="0" y2="1"><stop offset="0" stop-color="#5a4a42"/><stop offset="1" stop-color="#1f2636"/></linearGradient></defs><rect width="400" height="564" fill="url(#g2)"/></svg>

<section class="cell c1 r2 text-cell">
  <p class="date">3. 12. 2021, 19.30 Uhr:</p>
  <h2 class="title">Marlene Vogt, „Mord &amp; Merlot – Rum für den Nikolaus“</h2>
  <p class="desc left">Der Nikolaus hat's nicht leicht. Immerzu durch enge Schornsteine steigen, um verwöhnten Rotznasen die neueste Spielkonsole zu bringen – das schlaucht. Gut, wenn einem da die richtige Stärkung gereicht wird – z.B. in Form von Rum. Marlene Vogt serviert die schönsten, bösesten, schrägsten und hintergründigsten Geschichten zum Fest. Die Villa Morena kredenzt feine Weine und das goldene Feuerwasser. Frohe Weihnachten! (Lesung mit Weinverkostung)</p>
</section>
<svg class="cell c2 r2" role="img" aria-label="Foto der Sängerin vor einer Backsteinwand"><defs><linearGradient id="g3" x1="0" y1="0" x2="0" y2="1"><stop offset="0" stop-color="#9a6a58"/><stop offset=".5" stop-color="#7a5448"/><stop offset="1" stop-color="#2a2220"/></linearGradient></defs><rect width="400" height="564" fill="url(#g3)"/></svg>
<section class="cell c3 r2 text-cell">
  <p class="date">15. 1. 2022, 19.30 Uhr:</p>
  <h2 class="title">Ina Kessler &amp; Otto Brandl, Zwei Musiker, ein Abend</h2>
  <p class="desc">Ina Kessler schreibt Lieder, die dem rastlosen Geist der heutigen Zeit entgegen wirken. Ihren Zuhörern bringt sie nahe, was Lotta Wirbelwind und Freundesnetz gemeinsam haben, warum Gott den Tod von Plapper-Paula fürchtet und wieso Gras mampfende Kühe keinen Burnout kriegen. Otto Brandl ist einer der bedeutendsten Folk-Blues-Künstler des Landes. Er verbindet Poesie, virtuoses Gitarrenspiel und stampfenden Akustik-Blues zu einer exquisiten Mischung.</p>
</section>

<svg class="cell c1 r3" role="img" aria-label="Foto des Vorlesers mit Lampe und Büchern"><defs><radialGradient id="g4" cx=".55" cy=".55" r=".7"><stop offset="0" stop-color="#d8cfc6"/><stop offset=".5" stop-color="#8a4a3c"/><stop offset="1" stop-color="#1c1a1a"/></radialGradient></defs><rect width="400" height="569" fill="url(#g4)"/></svg>
<section class="cell c2 r3 text-cell">
  <p class="date">29. 1. 2022, 19.30 Uhr:</p>
  <h2 class="title">Rose Velours, „Der samtene Abend“ (Konzert)</h2>
  <p class="desc left">Seit 1998 steht der Name "Rose Velours" für moderne Adaptionen der großen Klassiker des französischen Chansons, aber auch für frische und freche Versionen von Songs aus der jungen Musikszene Frankreichs. Ein Abend voller „l'amour“, „l'esprit“ und „grandes emotions“. Vive la France!</p>
</section>
<svg class="cell c3 r3" role="img" aria-label="Foto einer alten Weinflasche mit roter Rose und Weinglas"><defs><linearGradient id="g5" x1="0" y1="0" x2="1" y2="0"><stop offset="0" stop-color="#8e8578"/><stop offset=".35" stop-color="#3a3b3d"/><stop offset=".8" stop-color="#4b4d4f"/><stop offset="1" stop-color="#8b1a1e"/></linearGradient></defs><rect width="400" height="569" fill="url(#g5)"/></svg>

<section class="cell c1 r4 text-cell">
  <p class="date" style="margin-top:20px">27. 1. 2022, 19.30 Uhr:</p>
  <h2 class="title">Tobias Rentz, „Geschichten vom Nachbartisch“ ... Erlesen komische Unterhaltung. Mit reichlich Heiter.</h2>
  <p class="desc">Rentz liest komische Geschichten von Karl Hensing bis Peter Wallbrecht. Liest vor? Nein, er atmet, lebt, schweigt, interpretiert mit vollem Körpereinsatz und faszinierender Mimik. Für diesen Abend hat er urkomische Geschichten zusammengetragen. Deren liebenswerte Protagonisten sind stets redlich bemüht, den Anforderungen des modernen Lebens gerecht zu werden und mit Anstand und Würde zu scheitern.</p>
</section>
<svg class="cell c2 r4" role="img" aria-label="Fotocollage der vier Bandmitglieder auf der Bühne"><defs><linearGradient id="g6" x1="0" y1="0" x2="1" y2="1"><stop offset="0" stop-color="#b5662a"/><stop offset=".5" stop-color="#5a3220"/><stop offset="1" stop-color="#c0702c"/></linearGradient></defs><rect width="400" height="553" fill="url(#g6)"/><line x1="208" y1="0" x2="208" y2="553" stroke="#fff" stroke-width="3"/><line x1="0" y1="284" x2="400" y2="284" stroke="#fff" stroke-width="3"/></svg>
<section class="cell c3 r4 quote-cell">
  <p class="quote">„Es sind die<br>Begegnungen<br>mit Menschen,<br>die das Leben<br>lebenswert<br>machen.“</p>
  <p class="quote-author">(Henri Lafarge)</p>
</section>

<div class="frame" style="left:38px;top:11px;height:1108px"></div>
<div class="frame" style="left:437px;top:11px;height:1108px"></div>
<div class="frame" style="left:836px;top:11px;height:1108px"></div>
<div class="frame" style="left:38px;top:1139px;height:1111px"></div>
<div class="frame" style="left:437px;top:1139px;height:1111px"></div>
<div class="frame" style="left:836px;top:1139px;height:1111px"></div>

<footer class="footer">
  <svg class="footer-photo" role="img" aria-label="Foto einer alten Weinflasche, Weinglas und roter Rose mit Spiegelung"><defs><linearGradient id="g7" x1="0" y1="0" x2="1" y2="0"><stop offset="0" stop-color="#8a8276"/><stop offset=".16" stop-color="#3d3e40"/><stop offset=".45" stop-color="#7a161b"/><stop offset=".7" stop-color="#4a4d4f"/><stop offset="1" stop-color="#4a4d4f"/></linearGradient></defs><rect width="760" height="583" fill="url(#g7)"/></svg>
  <div class="venue">
    <p class="venue-name">Villa<br>Morena</p>
    <p class="venue-tag">Kultursalon Bad Solmingen</p>
  </div>
  <p class="info" style="top:314px">„Kultur und Wein in der Villa Morena“</p>
  <p class="info" style="top:362px">Villa Morena, Lindenweg 7,<br>55543 Bad Solmingen</p>
  <p class="info" style="top:434px">Weitere Infos unter:<br>www.villa-morena-kulturhaus.de</p>
  <p class="info" style="top:504px">Tickets erhältlich bei:<br>Karten Direkt und den<br>angeschlossenen VVK-Stellen</p>
</footer>
<p class="sponsor-label">Mit freundlicher<br>Unterstützung durch:</p>
<div class="sponsor"><span class="sponsor-mark"></span><span class="sponsor-name">Kreisbank<br>Nahetal</span></div>

</body>
</html>
```